Stridewell Outfitters Stationary

At Stridewell Outfit, we know that rehab technology is much more than a tool or machine. It’s mobility for your body and productivity and freedom for your lifestyle to reclaim your life. That’s why we specialize in custom power and manual wheelchairs, scooters, complex seating and positioning, standers, and bathroom equipment that all help you reclaim your life.

Our rehab equipment includes custom power wheelchairs offering complex, customized seating and positioning systems with an array of specialized electronic control features. With a certified staff of Assistive Technology Professionals (ATPs) and technical repair department, we provide knowledgeable assistance to make sure you get the right products needed to reclaim your life – delivered on time, right to your door.

```html
<!DOCTYPE html>
<html lang="en">
<head>
<meta charset="utf-8">
<title>Stridewell Outfitters Letterhead</title>
<link href="https://fonts.googleapis.com/css2?family=Didact+Gothic&family=Arimo:wght@400;700&display=swap" rel="stylesheet">
<style>
  :root {
    --backdrop: #c3c8cb;
    --paper: #f3f3f3;
    --navy: #1b2c57;
    --green: #8cc43f;
    --ink: #4a4a4a;
    --ink-dark: #222;
    --signature-tone: #b9c2e6;
    --fold-mark: #c9c9c9;
  }
  * { margin: 0; padding: 0; box-sizing: border-box; }
  html, body { width: 1200px; height: 1000px; overflow: hidden; }
  body { background: var(--backdrop); position: relative; font-family: "Didact Gothic", sans-serif; }

  .letterhead {
    position: absolute; left: 290px; top: 69px; width: 623px; height: 879px;
    background: var(--paper);
  }
  .fold-mark { position: absolute; left: 0; width: 28px; height: 1px; background: var(--fold-mark); }
  .fold-mark--upper { top: 311px; }
  .fold-mark--lower { top: 622px; }

  .brand { position: absolute; left: 58px; top: 48px; display: flex; align-items: center; gap: 8px; }
  .brand__dot { width: 14px; height: 14px; border-radius: 50%; background: var(--green); }
  .brand__name { font-size: 23px; color: var(--navy); line-height: 1; letter-spacing: 0.2px; }

  .contact { position: absolute; left: 451px; top: 67px; font-family: "Arimo", sans-serif; font-size: 8.5px; color: var(--ink-dark); }
  .contact__row { display: flex; align-items: center; gap: 5px; height: 11.5px; }
  .contact__icon { width: 9px; height: 9px; }
  .contact__address { margin-top: 8px; line-height: 12px; }

  .letter { position: absolute; left: 58px; top: 294px; width: 506px; color: var(--ink); font-size: 9.6px; line-height: 11.2px; }
  .letter__greeting { font-family: "Arimo", sans-serif; font-weight: 700; color: var(--ink-dark); font-size: 9px; margin-bottom: 12px; }
  .letter__paragraph { text-align: justify; margin-bottom: 11px; }
  .letter__closing { margin-top: 12px; font-size: 9.4px; line-height: 11px; }
  .letter__signer { font-family: "Arimo", sans-serif; font-weight: 700; color: var(--ink-dark); font-size: 9px; }

  .signature { position: absolute; left: 133px; top: 556px; width: 128px; height: 62px; border-radius: 6px;
    background: linear-gradient(135deg, var(--signature-tone), rgba(185,194,230,0.35)); }

  .footer-band { position: absolute; left: 0; bottom: 0; width: 623px; height: 9px; }
</style>
</head>
<body>
  <main class="letterhead">
    <span class="fold-mark fold-mark--upper"></span>
    <span class="fold-mark fold-mark--lower"></span>

    <header>
      <div class="brand">
        <span class="brand__dot"></span>
        <span class="brand__name">Stridewell Outfitters</span>
      </div>

      <address class="contact" style="font-style:normal">
        <div class="contact__row">
          <svg class="contact__icon" viewBox="0 0 10 10"><rect width="10" height="10" rx="1.5" fill="#8cc43f"/><path d="M3 2.2l1.1 1.6-.6.8c.4.8 1 1.4 1.8 1.8l.8-.6 1.6 1.1-.6 1.1C5 7.9 2.3 5.2 2 3z" fill="#fff"/></svg>
          <span>+1 847-555-0142</span>
        </div>
        <div class="contact__row">
          <svg class="contact__icon" viewBox="0 0 10 10"><rect width="10" height="10" rx="1.5" fill="#8cc43f"/><rect x="2" y="3" width="6" height="4.2" fill="none" stroke="#fff" stroke-width=".8"/><path d="M2 3l3 2.3L8 3" fill="none" stroke="#fff" stroke-width=".8"/></svg>
          <span>hello@stridewell.com</span>
        </div>
        <div class="contact__row">
          <svg class="contact__icon" viewBox="0 0 10 10"><rect width="10" height="10" rx="1.5" fill="#8cc43f"/><circle cx="5" cy="5" r="3" fill="none" stroke="#fff" stroke-width=".7"/><ellipse cx="5" cy="5" rx="1.2" ry="3" fill="none" stroke="#fff" stroke-width=".6"/><path d="M2 5h6" stroke="#fff" stroke-width=".6"/></svg>
          <span>www.stridewell.com</span>
        </div>
        <div class="contact__address">410 Meadowbrook Park #220<br>Glenview IL 60025</div>
      </address>
    </header>

    <section class="letter">
      <p class="letter__greeting">Dear sir,</p>
      <p class="letter__paragraph">Communication is a very integral part of living creatures, animals and humans. Communication may be verbal or written. Written communication however is only applicable to human beings. Can you even imagine a world without communication? Verbal communication can be through telephones, webcams or in person. Written communication is through letters, emails and mobile phone messages.</p>
      <p class="letter__paragraph">In today’s world of great inventions and technology, letters have somehow become redundant. It is the time for text messages or chats. But they still can communicate a lot more than all other modes of communication. Organizations and various government departments still bank on letters as a strong medium of communication. There is no comparison in costs of sending letters as compared to costs of mobile phone messages though – letters are far cheaper. Letters now commonly known as “hard copy documents” are considered more relevant and important than email copies of text messages as proof or evidence of some sort.</p>
      <p class="letter__paragraph">Letters speak volumes about a person or an organization that writes it. So one must take utmost care ensuring that the language used in any letter is appropriate for the occasion for which it is being written. Since a letter is also a written proof or document, if there are certain things that should not form a part of it, then that too should be carefully handled.</p>
      <p class="letter__paragraph">Writing a good letter is an art. But if for some reason someone is unable to write that perfect letter, these different types of letters provide a base for you to build on. Sample letters have been given for everyone to understand what all information needs to form a part of the letter type and then it can be customized.</p>
      <p class="letter__closing">Yours Sincerely,<br><span class="letter__signer">Dana Whitlock</span></p>
    </section>

    <div class="signature" role="img" aria-label="Handwritten signature of the sender"></div>

    <svg class="footer-band" viewBox="0 0 623 9" preserveAspectRatio="none">
      <polygon points="0,0 423,0 414,9 0,9" fill="#1b2c57"/>
      <polygon points="428,0 623,0 623,9 419,9" fill="#8cc43f"/>
    </svg>
  </main>
</body>
</html>
```